Medical Billing Business needs a web page designed

We need a web page for a new medical billing business for prospective clients to go to to get information about our company. It needs to show what our company stands for and our billing rates. Our colors are blue, gray and white. I have attached our logo, brochure and mission statement.

Need tabs at top for "about us", "contact us" "specials". On contact page, need a form to fill out that will be automatically emailed to us upon completion. Under specials...Sign a contract by the end of August 2014 and receive one month of billing FREE. ***Receive 25% off the first 4 months of the contract***

Medical

```html
<!DOCTYPE html>
<html lang="en">
<head>
<meta charset="utf-8">
<title>Prairie Claims Billing, LLC</title>
<link href="https://fonts.googleapis.com/css2?family=Arimo:ital,wght@0,400;0,700;1,400&family=Bitter:wght@400&family=Open+Sans:wght@600&display=swap" rel="stylesheet">
<style>
:root{
  --navy:#0d2e42;
  --teal:#1bb8d0;
  --teal-dark:#138ea3;
  --ink:#222;
  --grey:#5d5d5d;
  --dark:#1e1e1e;
  --footer:#222324;
  --page:#e9ebed;
  --white:#fff;
  --red:#e41c1c;
}
*{box-sizing:border-box;margin:0;padding:0}
html,body{width:1043px;height:1200px;overflow:hidden}
body{position:relative;background:var(--page);font-family:"Arimo",Arial,sans-serif;color:var(--ink)}
.abs{position:absolute}
.top-bar{left:0;top:0;width:1043px;height:29px;background:var(--navy);color:var(--white);font-size:11px;font-weight:700;text-align:right;padding:8px 176px 0 0}
.top-rule{left:0;top:30px;width:1043px;height:3px;border-top:1px solid var(--navy);border-bottom:1px solid var(--navy)}
.header{left:0;top:33px;width:1043px;height:104px;background:var(--white)}
.brand{left:181px;top:62px;display:flex;align-items:center;gap:7px}
.brand-mark{width:18px;height:18px;background:var(--teal)}
.brand-name{font-size:17px;font-weight:700;color:var(--teal-dark)}
.question{left:602px;top:56px;font-size:15px;color:var(--grey)}
.phone-icon{left:723px;top:52px}
.phone-top{left:755px;top:51px;font-size:19px;color:var(--teal)}
.nav{left:546px;top:103px;display:flex;font-size:12px;font-weight:700;color:var(--ink)}
.nav a{display:block;height:33px;line-height:33px;text-decoration:none;color:inherit;padding:0 10px}
.nav a.active{background:var(--teal);color:var(--white);padding:0 18px}
.hero-band{left:0;top:137px;width:1043px;height:317px;background:#1b1b1b}
.hero-photo{left:171px;top:137px;width:700px;height:317px;background:linear-gradient(90deg,#8a8f92 0%,#c9ccce 35%,#e8e6e3 55%,#a8b0b4 80%,#6e7a80 100%)}
.hero-caption{left:171px;top:415px;width:700px;height:39px;background:rgba(110,130,140,.65);font-family:"Bitter",Georgia,serif;font-size:29px;color:var(--white);padding:0 0 0 6px;line-height:39px}
.hero-caption em{font-style:normal;color:var(--red)}
.slider-dots{left:805px;top:429px;display:flex;gap:4px}
.slider-dots span{width:11px;height:11px;border-radius:50%;border:1.5px solid #ccc}
.slider-dots span:first-child{background:#333;border-color:#111}
.page-body{left:171px;top:454px;width:700px;height:566px;background:var(--white)}
.services{left:171px;top:454px;width:700px;height:164px;background:var(--dark)}
.services-tab{left:421px;top:454px;width:200px;height:29px;background:#5a5e60;clip-path:polygon(0 0,100% 0,93% 100%,7% 100%);color:var(--white);font-size:20px;text-align:center;line-height:27px}
.rate-card{top:501px;width:222px;height:98px;background:var(--white);border-radius:4px;padding:7px 6px}
.rate-card h3{font-size:17px;font-weight:700;color:var(--teal);margin-bottom:4px;white-space:nowrap}
.rate-grid{display:grid;grid-template-columns:128px 18px auto;font-size:13px;line-height:20px;white-space:nowrap}
.band-shadow{left:171px;top:618px;width:700px;height:10px;background:radial-gradient(ellipse at top,rgba(0,0,0,.35),rgba(0,0,0,0) 70%)}
.stray-tick{left:120px;top:724px}
.panel{top:655px;width:204px;height:213px;background:linear-gradient(#fff 80%,#ececec);border:1px solid #ddd;border-radius:5px}
.panel-head{position:absolute;left:-5px;top:6px;width:211px;height:31px;background:linear-gradient(#2b2b2b,#050505);color:var(--white);font-size:19px;line-height:31px;padding-left:44px;white-space:nowrap}
.panel-icon{position:absolute;left:0;top:0;width:32px;height:31px;background:var(--teal);display:flex;align-items:center;justify-content:center}
.panel-body{position:absolute;left:10px;top:52px;right:10px;font-size:10px;line-height:12px;color:#333}
.panel-body.justify{text-align:justify;font-size:9.5px}
.panel-body .offer{font-style:italic;margin-top:8px;line-height:14px}
.btn{position:absolute;left:10px;top:185px;height:21px;padding:0 7px;background:var(--teal);color:var(--white);font-size:10px;font-weight:700;line-height:21px}
.field{position:absolute;left:9px;width:188px;height:25px;border:1px solid #ddd;font-size:9px;color:#444;line-height:23px;padding-left:21px}
.field svg{position:absolute;left:6px;top:7px}
.clients-title{left:174px;top:907px;font-family:"Open Sans",Arial,sans-serif;font-weight:600;font-size:18px;color:#333}
.clients-rule{left:174px;top:931px;width:693px;border-top:1px dashed #aaa}
.clients-arrows{left:828px;top:913px}
.client-row{left:176px;top:950px;width:694px;display:flex;justify-content:space-between;align-items:center;height:32px}
.client-row span{font-size:19px;font-weight:700;color:#555}
.client-row span.light{font-weight:400;color:#888}
.footer{left:0;top:1020px;width:1043px;height:148px;background:var(--footer);color:var(--white)}
.foot-title{position:absolute;top:19px;font-size:13px;font-weight:400;padding-bottom:7px;border-bottom:1px dotted #666}
.quick-links{position:absolute;left:174px;top:51px;list-style:none;font-size:10px;line-height:17px}
.quick-links li::before{content:"›";color:#888;margin-right:8px}
.newsletter-text{position:absolute;left:294px;top:55px;font-size:13px;line-height:16px;width:220px}
.email-input{position:absolute;left:295px;top:94px;width:143px;height:21px;background:var(--white);border-radius:3px;font-size:9px;font-style:italic;color:#777;padding:5px 7px}
.subscribe{position:absolute;left:443px;top:94px;width:66px;height:21px;background:var(--teal);font-size:10px;font-weight:700;text-align:center;line-height:21px}
.contact-item{position:absolute;left:553px;display:flex;gap:9px;font-size:10px;line-height:15px}
.contact-item .big{font-size:12px}
.foot-brand{position:absolute;left:745px;top:80px;display:flex;align-items:center;gap:6px;font-size:15px;font-weight:700;color:var(--teal)}
.foot-brand i{width:12px;height:12px;background:var(--teal)}
.col-rule{position:absolute;top:20px;width:1px;height:110px;background:#333}
.bottom-bar{left:0;top:1168px;width:1043px;height:32px;background:var(--navy);color:var(--white);font-size:9.5px;text-align:center;line-height:32px}
</style>
</head>
<body>
<div class="abs top-bar">Contact us Today. We're here for you 7 days a week</div>
<div class="abs top-rule"></div>

<header class="abs header"></header>
<div class="abs brand"><span class="brand-mark"></span><span class="brand-name">Prairie Claims Billing, LLC</span></div>
<div class="abs question">Have a Question?</div>
<svg class="abs phone-icon" width="24" height="24" viewBox="0 0 24 24" aria-hidden="true"><circle cx="12" cy="12" r="10.5" fill="none" stroke="#1bb8d0" stroke-width="1.5"/><path d="M9 7c-1.5 1-1.5 4 .5 7s4 4 5.5 3l1-1.5-2-1.5-1 1c-1-.5-2.5-2.5-2.8-3.6l1-.8-1-2.4z" fill="#1bb8d0"/></svg>
<div class="abs phone-top">800-555-0142</div>
<nav class="abs nav">
  <a class="active" href="#">HOME</a>
  <a href="#">ABOUT US</a>
  <a href="#" style="padding-left:20px">SPECIALS</a>
  <a href="#" style="padding-left:22px">CONTACT US</a>
</nav>

<div class="abs hero-band"></div>
<div class="abs hero-photo" role="img" aria-label="Photo of three smiling doctors in white coats with stethoscopes"></div>
<div class="abs hero-caption">Enhance And <em>Improve</em> Your Collection Rate</div>
<div class="abs slider-dots"><span></span><span></span><span></span><span></span></div>

<div class="abs page-body"></div>
<section class="abs services"></section>
<div class="abs services-tab">Services We Offer</div>
<div class="abs rate-card" style="left:186px">
  <h3>Billing Service</h3>
  <div class="rate-grid">
    <span>$150,001</span><span>--</span><span>&lt; 5%</span>
    <span>$100,001 - $150,000</span><span>--</span><span>5.5%</span>
    <span>$80,001 - $ 100, 000</span><span>--</span><span>5.75%</span>
  </div>
</div>
<div class="abs rate-card" style="left:634px">
  <h3>Billing &amp; Coding Services</h3>
  <div class="rate-grid">
    <span>$150,001</span><span>--</span><span>&lt; 6%</span>
    <span>$100,001 - $150,000</span><span>--</span><span>&nbsp;6.5 %</span>
    <span>$80,001 - $100,000</span><span>--</span><span>&nbsp;6.75 %</span>
  </div>
</div>
<div class="abs band-shadow"></div>

<svg class="abs stray-tick" width="12" height="10" viewBox="0 0 12 10" aria-hidden="true"><path d="M1 5l3 3 7-7" fill="none" stroke="#6aa622" stroke-width="2"/></svg>

<article class="abs panel" style="left:188px">
  <div class="panel-head"><span class="panel-icon"><svg width="16" height="18" viewBox="0 0 16 18"><rect x="2" y="2" width="12" height="14" fill="#fff"/></svg></span>Welcome to PCB</div>
  <p class="panel-body justify">Our mission at Prairie Claims Billing, LLC is to set the standard of excellence for providing quality medical administrative services to our clients. Our company's success, which is characterized by organizational excellence as well as our responsiveness of our client's needs, has been founded on our customer service. Our clients and their patients will trust....</p>
  <span class="btn">READ MORE</span>
</article>
<article class="abs panel" style="left:418px">
  <div class="panel-head"><span class="panel-icon"><svg width="14" height="20" viewBox="0 0 14 20"><circle cx="7" cy="6" r="5" fill="none" stroke="#fff" stroke-width="2"/><path d="M3 10l-1 9 5-3 5 3-1-9" fill="#fff"/></svg></span>About Our Specials</div>
  <div class="panel-body" style="top:46px">
    <p style="line-height:14px">Lorem ipsum dolor sit amet, consctetuer adipiscing elit, sed diam nonummy nibh euismod tincidunt ut laoreet dolor re rera ema gn liquam erat volutpat. Ut wisi nim ad minim veniam.</p>
    <p class="offer">Sign a contract by the end of August 2014 and receive one month of billing FREE. ***Receive 25% off the first 4 months of the contract***.......</p>
  </div>
  <span class="btn">READ MORE</span>
</article>
<article class="abs panel" style="left:649px">
  <div class="panel-head"><span class="panel-icon"><svg width="18" height="12" viewBox="0 0 18 12"><rect x="0" y="0" width="18" height="12" fill="#fff"/><path d="M0 0l9 7 9-7" fill="none" stroke="#1bb8d0" stroke-width="1.5"/></svg></span>Quick Contact</div>
  <div class="field" style="top:49px"><svg width="9" height="10" viewBox="0 0 9 10"><circle cx="4.5" cy="3" r="2.5" fill="#999"/><path d="M0 10c0-3 2-4.5 4.5-4.5S9 7 9 10z" fill="#999"/></svg>Name</div>
  <div class="field" style="top:79px"><svg width="10" height="8" viewBox="0 0 10 8"><rect width="10" height="8" fill="#999"/><path d="M0 0l5 4 5-4" fill="none" stroke="#fff"/></svg>Email</div>
  <div class="field" style="top:110px;height:59px"><svg width="10" height="10" viewBox="0 0 10 10"><rect x=".5" y="1.5" width="8" height="8" fill="none" stroke="#999"/><path d="M4 6l5-5" stroke="#999" stroke-width="1.5"/></svg>Message</div>
  <span class="btn">SUBMIT</span>
</article>

<h2 class="abs clients-title">Our Clients</h2>
<div class="abs clients-rule"></div>
<svg class="abs clients-arrows" width="30" height="14" viewBox="0 0 30 14" aria-hidden="true"><path d="M7 2l-5 5 5 5" fill="none" stroke="#555" stroke-width="1.5"/><path d="M22 2l5 5-5 5" fill="none" stroke="#1bb8d0" stroke-width="1.5"/></svg>
<div class="abs client-row">
  <span>Northwind</span><span class="light">Cloudhaven</span><span>Arcline</span><span>Brightwave</span><span class="light">Cloudhaven</span><span>Arcline</span>
</div>

<footer class="abs footer">
  <h4 class="foot-title" style="left:174px">Quick Links</h4>
  <ul class="quick-links"><li>Home</li><li>About Us</li><li>Specials</li><li>FAQ's</li><li>Contact Us</li></ul>
  <div class="col-rule" style="left:270px"></div>
  <h4 class="foot-title" style="left:294px;width:150px">Subscribe to Newsletter</h4>
  <p class="newsletter-text">Get the lastet offers &amp; prices directly in your mail box</p>
  <div class="email-input">Email address</div>
  <div class="subscribe">SUBSCRIBE</div>
  <div class="col-rule" style="left:527px"></div>
  <h4 class="foot-title" style="left:553px;width:148px">Contact Details</h4>
  <div class="contact-item" style="top:50px"><svg width="9" height="12" viewBox="0 0 9 12"><path d="M4.5 0A4.5 4.5 0 0 0 0 4.5C0 8 4.5 12 4.5 12S9 8 9 4.5A4.5 4.5 0 0 0 4.5 0z" fill="#fff"/><circle cx="4.5" cy="4.5" r="1.6" fill="#222"/></svg><span>410 N Elm Street,<br>Ashford, KS 66000</span></div>
  <div class="contact-item" style="top:92px"><svg width="10" height="12" viewBox="0 0 10 12"><path d="M2 0C0 1 0 5 2.5 8.5S8 13 9.5 11.5l.5-1.5-2.5-1.5-1 1C5.5 9 3.5 6.5 3.5 5l1-.8L3.5 0z" fill="#fff"/></svg><span class="big">800-555-0142</span></div>
  <div class="contact-item" style="top:116px"><svg width="10" height="8" viewBox="0 0 10 8" style="margin-top:3px"><rect width="10" height="8" fill="#fff"/><path d="M0 0l5 4 5-4" fill="none" stroke="#222"/></svg><span class="big">ana@prairieclaims.com<br>ben@prairieclaims.com</span></div>
  <div class="col-rule" style="left:720px"></div>
  <div class="foot-brand"><i></i>Prairie Claims</div>
</footer>
<div class="abs bottom-bar">© Copyright 2014 PrairieClaimsBilling, LLC. &nbsp; | &nbsp; All Rights Reserved</div>
</body>
</html>
```